Tech business card design

We need an amazing business card design for our new business 'Brakka' a marketing tech startup based in Sydney, Australia. We provide an online marketplace for businesses to search and buy advertising media, connect with service providers and learn more about marketing. We wish to communicate 'cool tech', reliability and professionalism and design based around our logo.

Target Market(s)

Business Owners

Contact Information for Business Card

Name
Position
Email Address
Website
Phone Number

Font styles to use
Other font styles liked:
• Avenir & Avenir Next

Colors

Designer to choose colors to be used in the design.

```html
<!DOCTYPE html>
<html lang="en">
<head>
<meta charset="utf-8">
<title>Brakka Business Card</title>
<link rel="stylesheet" href="https://fonts.googleapis.com/css2?family=Mulish:wght@400;600;800&display=swap">
<style>
  :root {
    --stage: #d4d7d7;
    --paper: #f6f6f4;
    --navy: #1c1a4d;
    --navy-soft: #2a2862;
    --white: #ffffff;
    --ink-muted: #2b2b3a;
  }
  * { margin: 0; padding: 0; box-sizing: border-box; }
  html, body { width: 1200px; height: 800px; overflow: hidden; }
  body {
    background: var(--stage);
    font-family: "Mulish", sans-serif;
    position: relative;
  }
  .card {
    position: absolute;
    top: 252px;
    width: 520px;
    height: 297px;
    overflow: hidden;
    box-shadow: 0 12px 28px rgba(0,0,0,0.18);
  }
  /* Front */
  .card-front { left: 50px; background: var(--paper); }
  .front-wordmark {
    position: absolute;
    left: 24px; top: 58px;
    font-weight: 800;
    font-size: 78px;
    line-height: 1;
    letter-spacing: -2px;
    color: var(--navy);
  }
  .front-name-row {
    position: absolute;
    left: 24px; top: 142px;
    right: 0;
    display: flex;
    align-items: flex-end;
  }
  .front-name {
    font-weight: 400;
    font-size: 30px;
    line-height: 1;
    letter-spacing: 0.5px;
    color: var(--navy);
    text-transform: uppercase;
    white-space: nowrap;
  }
  .title-band {
    flex: 1;
    margin-left: 6px;
    height: 18px;
    background: var(--navy);
    color: var(--white);
    font-size: 9px;
    font-weight: 600;
    letter-spacing: 0.6px;
    display: flex;
    align-items: center;
    padding-left: 6px;
  }
  .contact-list {
    position: absolute;
    left: 24px; right: 24px; top: 192px;
    display: flex;
    justify-content: space-between;
    list-style: none;
    font-size: 11px;
    color: var(--ink-muted);
  }
  .contact-item { display: flex; align-items: center; gap: 6px; }
  .contact-item svg { width: 13px; height: 13px; fill: var(--navy); }
  .base-band {
    position: absolute;
    left: 0; right: 0; top: 232px;
    height: 22px;
    background: var(--navy);
  }
  /* Back */
  .card-back { left: 630px; background: var(--navy); }
  .back-pattern {
    position: absolute; inset: 0;
    background: linear-gradient(135deg, var(--navy) 0%, var(--navy-soft) 50%, var(--navy) 100%);
  }
  .back-identity {
    position: absolute; inset: 0;
    display: flex; flex-direction: column;
    align-items: center; justify-content: center;
    color: var(--white);
  }
  .back-wordmark {
    font-weight: 800;
    font-size: 56px;
    line-height: 1;
    letter-spacing: -1.5px;
  }
  .back-name {
    margin-top: 8px;
    font-weight: 400;
    font-size: 18px;
    letter-spacing: 1px;
    text-transform: uppercase;
  }
</style>
</head>
<body>
  <section class="card card-front">
    <div class="front-wordmark">brakka</div>
    <div class="front-name-row">
      <span class="front-name">Mara Linden</span>
      <span class="title-band">OWNER/CEO</span>
    </div>
    <ul class="contact-list">
      <li class="contact-item">
        <svg viewBox="0 0 24 24" aria-hidden="true"><path d="M6.6 10.8a15 15 0 0 0 6.6 6.6l2.2-2.2c.3-.3.7-.4 1-.2 1.1.4 2.3.6 3.6.6.6 0 1 .4 1 1V20c0 .6-.4 1-1 1A17 17 0 0 1 3 4c0-.6.4-1 1-1h3.5c.6 0 1 .4 1 1 0 1.3.2 2.5.6 3.6.1.3 0 .7-.2 1z"/></svg>
        555.013.2847
      </li>
      <li class="contact-item">
        <svg viewBox="0 0 24 24" aria-hidden="true"><path d="M2 5h20v14H2z M4 7v.4l8 5.2 8-5.2V7z" fill-rule="evenodd"/></svg>
        mara.linden@brakka.com
      </li>
      <li class="contact-item">
        <svg viewBox="0 0 24 24" aria-hidden="true"><circle cx="12" cy="12" r="10"/></svg>
        www.brakka.com
      </li>
    </ul>
    <div class="base-band"></div>
  </section>

  <section class="card card-back">
    <div class="back-pattern" role="img" aria-label="Faint repeating brand pattern across the card background"></div>
    <div class="back-identity">
      <div class="back-wordmark">brakka</div>
      <div class="back-name">Mara Linden</div>
    </div>
  </section>
</body>
</html>
```